International Educational/Tuition/Learning Center

Company Background:
- Business card for a educational/tuition/learning center that provides supplementary lessons for students in Grade 7 to 12 ( Secondary and JC syllabus in the GCE 'O' and GCE 'A' level context but not limited to these. Future plans will be to cater for SAT, IB and HSCs programs.
- Name of company is called "THE QUILL AND LANTERN".
- Vision is to complement the basic principles of the rote learning culture and value-add by training the students to think out of the box and preserve creativity.
- To re-define and retain the value of the learning process.

Sketch Design:
- Simple and classy design that is mainly white-based with tinge of refreshing bright lime green.
- "New Age" simple and classy design that appeals to teenagers and young adults.
- Logo design to reinforce the vision of company.

Rough idea of what we have in mind but pls do not let this restrict your creativity:
- White and bright green base
- 2 sided print
- Front with simple information of Name and Designation as well as de-bossed/letterpressed print
- Details of on reverse side
- Contact details can be categorized as " find me" - address, "call me" - contact number , "email me" - email address, " Find out more"- website.

Information:

Name: Darel K Thuam
Title: Managing Director
Address: 41 Pelham Crescent, #07-15, Singapore 654321
Contact: +65 91234056
Email: darelthuam@mailvesta.com
Website: www.qnl-tutor.com

Thank you all in advance! Looking forward to some amazing designs from all you talented folks!
Updates

hi all,

have updated the projected to a guranteed status from the initial refundable status.

Thanks 

Dear designers,

I've included more info into the brief on design elements to include. 

Thanks for your participation and efforts!

Cheers!

Target Market(s)

young parents with school going children

Industry/Entity Type

Training

Requirements
Must have
• debossed/letterpressed logo
feel free to be creative with ur designs!
Nice to have
• round edges
Logo/name could have some elements of education/knowledge/path-to-learning incorporated in the design concept

```html
<!DOCTYPE html>
<html lang="en">
<head>
<meta charset="utf-8">
<title>The Quill and Lantern – Business Card</title>
<link rel="stylesheet" href="https://fonts.googleapis.com/css2?family=Righteous&family=Quicksand:wght@300&family=Open+Sans:wght@400;600&display=swap">
<style>
  :root {
    --backdrop: #e6e6e6;
    --card: #ffffff;
    --lime: #9cf000;
    --lime-deep: #7fd100;
    --lime-soft: rgba(156, 240, 0, 0.16);
    --ink: #111111;
    --ink-soft: #3a3a3a;
    --pattern: rgba(0, 0, 0, 0.045);
  }
  * { box-sizing: border-box; margin: 0; padding: 0; }
  html, body {
    width: 1200px;
    height: 900px;
    overflow: hidden;
    background: var(--backdrop);
  }
  .stage { position: relative; width: 1200px; height: 900px; }

  .card {
    position: absolute;
    width: 540px;
    height: 320px;
    background: var(--card);
    overflow: hidden;
    box-shadow: 0 3px 8px rgba(0, 0, 0, 0.25);
  }

  /* ---------- Details side ---------- */
  .card--details { left: 40px; top: 400px; }
  .details__band {
    position: absolute; top: 0; right: 0; width: 38px; height: 100%;
    background: linear-gradient(90deg, var(--lime), var(--lime-deep));
  }
  .details__doodles {
    position: absolute; top: 10px; right: 48px; width: 200px; height: 300px;
    border-radius: 14px;
    background: radial-gradient(ellipse at 60% 45%, var(--lime-soft), rgba(156, 240, 0, 0.04) 75%);
  }
  .details__name {
    position: absolute; left: 40px; top: 82px;
    font-family: "Righteous", sans-serif;
    font-size: 38px; line-height: 1; color: var(--ink);
    text-transform: uppercase; letter-spacing: 0.5px;
  }
  .details__title {
    position: absolute; left: 42px; top: 122px;
    font-family: "Righteous", sans-serif;
    font-size: 19px; line-height: 1; color: var(--ink);
    text-transform: uppercase;
  }
  .details__list {
    position: absolute; left: 48px; top: 178px;
    list-style: none;
    font-family: "Open Sans", sans-serif;
    font-size: 13.5px; line-height: 21px;
    text-transform: uppercase; color: var(--ink-soft);
  }
  .details__label { font-weight: 600; color: var(--ink); }

  /* ---------- Front side ---------- */
  .card--front { left: 620px; top: 100px; }
  .front__pattern {
    position: absolute; inset: 0 0 36px 0;
    background: linear-gradient(135deg, var(--pattern), rgba(0,0,0,0.015) 50%, var(--pattern));
  }
  .front__band {
    position: absolute; left: 0; bottom: 0; width: 100%; height: 36px;
    background: linear-gradient(180deg, var(--lime-deep), var(--lime));
  }
  .front__text {
    position: absolute; left: 0; top: 62px; width: 100%;
    text-align: center; color: var(--lime);
  }
  .front__name {
    font-family: "Righteous", sans-serif;
    font-size: 54px; line-height: 1; text-transform: uppercase;
  }
  .front__title {
    margin-top: 6px;
    font-family: "Righteous", sans-serif;
    font-size: 25px; line-height: 1; text-transform: uppercase;
    color: var(--lime-deep);
  }
  .front__company {
    margin-top: 14px;
    font-family: "Quicksand", sans-serif;
    font-weight: 300; font-size: 30px; letter-spacing: 3px;
    color: var(--lime-deep);
  }
</style>
</head>
<body>
<main class="stage">

  <section class="card card--details">
    <div class="details__doodles" role="img" aria-label="Lime line doodles of school items: apple, ruler, scroll, letters, numbers, mortarboard, pencil, music note"></div>
    <div class="details__band"></div>
    <h1 class="details__name">Darel K Thuam</h1>
    <p class="details__title">Managing Director</p>
    <ul class="details__list">
      <li><span class="details__label">Address:</span> 41 Pelham Crescent, #07-15, Singapore 654321</li>
      <li><span class="details__label">Contact:</span> +65 91234056</li>
      <li><span class="details__label">Email:</span> darelthuam@mailvesta.com</li>
      <li><span class="details__label">Website:</span> www.qnl-tutor.com</li>
    </ul>
  </section>

  <section class="card card--front">
    <div class="front__pattern" role="img" aria-label="Faint grey pattern of school doodles: numbers, apples, mortarboards, pencils, music notes"></div>
    <div class="front__text">
      <h2 class="front__name">Darel K Thuam</h2>
      <p class="front__title">Managing Director</p>
      <p class="front__company">QNL</p>
    </div>
    <div class="front__band"></div>
  </section>

</main>
</body>
</html>
```